KPT Building And Maintenance

Need a very professional looking double sided Buisiness card with all my details phone number, name, email, license number.

Target Market(s)

construction industry

Industry/Entity Type

building

Contact Information for Business Card

Name Dale Whitcombe. Email Address Info@KPTBuilding.example.au mobile number 0452918730 licence number 871406D. web site

```html
<!DOCTYPE html>
<html lang="en">
<head>
<meta charset="utf-8">
<title>KPT Building And Maintenance – Business Card</title>
<link rel="stylesheet" href="https://fonts.googleapis.com/css2?family=Montserrat:wght@400;500;800&display=swap">
<style>
  :root {
    --bg: #d1d2d4;
    --card: #ffffff;
    --blue: #4a9bd8;
    --ink: #4b4b4d;
    --ink-soft: #555557;
  }
  html, body {
    margin: 0;
    width: 1200px;
    height: 1200px;
    overflow: hidden;
    background: var(--bg);
    font-family: "Montserrat", Arial, sans-serif;
  }
  .card {
    position: absolute;
    left: 247px;
    width: 705px;
    height: 402px;
    background: var(--card);
    border-radius: 28px;
    overflow: hidden;
  }
  .card--front { top: 147px; }
  .card--back { top: 650px; }

  .rule {
    position: absolute;
    height: 2px;
    background: var(--blue);
  }

  /* front */
  .front-rule-left { left: 0; width: 78px; top: 146px; }
  .front-rule-right { left: 290px; width: 384px; top: 146px; }
  .brand-name {
    position: absolute;
    left: 98px;
    width: 172px;
    top: 134px;
    margin: 0;
    text-align: center;
    font-weight: 800;
    font-size: 20px;
    line-height: 26px;
    color: var(--ink);
    white-space: nowrap;
  }
  .person {
    position: absolute;
    right: 31px;
    top: 105px;
    text-align: right;
  }
  .person-name {
    margin: 0;
    font-size: 32px;
    font-weight: 500;
    line-height: 40px;
    color: var(--ink);
    text-transform: uppercase;
    letter-spacing: -0.2px;
  }
  .person-name .first { color: var(--blue); }
  .person-role {
    margin: 0;
    font-size: 19px;
    line-height: 24px;
    font-weight: 400;
    letter-spacing: 1px;
    color: var(--ink-soft);
  }
  .contacts {
    position: absolute;
    right: 31px;
    top: 203px;
    margin: 0;
    padding: 0;
    list-style: none;
  }
  .contact {
    display: flex;
    justify-content: flex-end;
    align-items: center;
    height: 22px;
    margin-bottom: 20px;
    font-size: 18px;
    letter-spacing: 1px;
    color: var(--ink-soft);
  }
  .contact:nth-child(2) { margin-bottom: 20px; }
  .contact svg { width: 22px; height: 22px; margin-left: 16px; flex: none; }

  /* back */
  .back-rule-left { left: 0; width: 163px; top: 200px; }
  .back-rule-right { left: 543px; width: 162px; top: 200px; }
  .back-brand {
    position: absolute;
    left: 181px;
    width: 344px;
    top: 180px;
    margin: 0;
    text-align: center;
    font-weight: 800;
    font-size: 36px;
    line-height: 42px;
    color: var(--ink);
    white-space: nowrap;
  }
</style>
</head>
<body>

<section class="card card--front" aria-label="Business card front">
  <div class="rule front-rule-left"></div>
  <p class="brand-name">KPT BUILDING</p>
  <div class="rule front-rule-right"></div>

  <div class="person">
    <h1 class="person-name"><span class="first">Dale</span> Whitcombe</h1>
    <p class="person-role">OWNER</p>
  </div>

  <ul class="contacts">
    <li class="contact">0452918730
      <svg viewBox="0 0 22 22" aria-hidden="true"><circle cx="11" cy="11" r="9.5" fill="none" stroke="#4a9bd8" stroke-width="2"/><path d="M7.5 6.5l2 0 1 2.5-1.3 1a6 6 0 0 0 2.8 2.8l1-1.3 2.5 1v2c-4.5 0.5-8.5-3.5-8-8z" fill="#4a9bd8"/></svg>
    </li>
    <li class="contact">www.kptbuilding.example.au
      <svg viewBox="0 0 22 22" aria-hidden="true"><circle cx="11" cy="11" r="10" fill="#4a9bd8"/><path d="M4 8c2 0 3 1 4 3s-1 3 0 5M12 3c1 2 3 2 4 4s-2 3 0 5 3 1 3 1" fill="none" stroke="#fff" stroke-width="1.6"/></svg>
    </li>
    <li class="contact">Info@KPTBuilding.example.au
      <svg viewBox="0 0 22 22" aria-hidden="true"><rect x="1" y="5" width="20" height="13" fill="#4a9bd8"/><path d="M1.5 5.5l9.5 7 9.5-7" fill="none" stroke="#fff" stroke-width="1.4"/></svg>
    </li>
    <li class="contact">871406D
      <svg viewBox="0 0 22 22" aria-hidden="true"><path d="M4 1h10l4 4v16H4z" fill="none" stroke="#4a9bd8" stroke-width="1.6"/><path d="M7 6h5M7 9h8M7 12h8M7 15h3M12 15h3M7 18h3M12 18h3" stroke="#4a9bd8" stroke-width="1.4"/></svg>
    </li>
  </ul>
</section>

<section class="card card--back" aria-label="Business card back">
  <div class="rule back-rule-left"></div>
  <p class="back-brand">KPT BUILDING</p>
  <div class="rule back-rule-right"></div>
</section>

</body>
</html>
```